WISP Laser Hair Removal Information Flyer

I’m looking to have a (tri-fold?) flyer created to provide some information about my laser Hair Removal business. I would like to include my logo (uploaded) as well as the following information:

WISP Laser Hair Removal Prices:

FACE
Upper Lip: $35
Chin: $35
Cheeks: $35
Full Face (Lip/Chin/Cheeks) - $100
Middle Brow: $25

UPPER BODY (above waist)
Underarm: $75
Chest: $150
Full Arm: $150
1/2 Arm: $100
Areola: $50
Full Back: $250
Shoulders: $75
Full Hands w/ Fingers: $50
Fingers only: $25

LOWER BODY (below waist)
Full Leg: $300
Upper Leg: $175
Lower Leg: $150
Stomach: $150
Navel and Navel Line: $50
Navel and Lower Abdomen: $100
Lower Back: $100
Classic Bikini: $75
Deep Bikini or Brazilian: $125
Buttocks: $100
Between cheeks: $75
Full Feet w/ Toes: $50
Toes Only: $25

Women (common combinations)
Full Arm w/ Underarm: $200
Full Leg w/ Classic Bikini: $350
Full Leg w/ Deep Bikini or Brazilian: $375
Classic Bikini w/ Inner Thigh: $100
Deep Bikini or Brazilian w/ Inner Thigh: $150

Men (common areas and combinations)
1/2 Face & Neck (front): $100
Cheeks & Neck (front): $75
Full Neck: $75
Nape of Neck: $50
Shoulders: $75
Full Back: $250
Full Back & Full Neck: $300
Neck (nape) and Shoulders: $100
Full Back, Neck and Buttocks: $375

Laser Hair Removal is an affordable, safe and effective way to treat unwanted hair - permanently!

WISP uses the Corvana GlideMark(TM) Diode Laser - the Gold Standard in Laser Hair Removal!

Wisp Laser Hair Removal with the Corvana GlideMark (TM):

The Corvana aesthetic division is a worldwide leader in energy-based aesthetic devices with presence in over 100 countries, as a pioneer in the field of aesthetic medicine. GlideMark (TM) is FDA approved and uses clinically proven diode laser technology to permanently remove unwanted hair comfortably, safely and effectively, for all skin colours and types - even with a tan.

How It works:
The GlideMark (TM) is able to stop the growth of unwanted hair permanently, by delivering high-energy pulses to the hair follicle. This is achieved by targeting the melanin inside the follicle and heating it up until follicle damage occurs. Treatments are made comfortable by the patented Frost Nib Integrated Technology; a system that continuously cools the skin of the area being treated.

What to expect:
Laser Hair Removal requires multiple sessions (typically between 6 - 8), spaced approximately 6 weeks between each session.

For more information, visit us at
www.wisplaser-example.ca
IG:
@wisplaserdemo

Find us on Facebook - WISP Laser Demo

Wisp is proudly partnered with the Maplegrove Aesthetic Clinic
4860 Tollway Crescent, Suite 115
London, ON

Contact WISP today for your complimentary consultation!

Marisol@wisplaser-example.ca
555-013-8826

* if the uploaded logo is not the right format, please let me know and I will upload a new file *

```html
<!DOCTYPE html>
<html lang="en">
<head>
<meta charset="utf-8">
<title>WISP Laser Hair Removal – Tri-fold Flyer</title>
<link rel="stylesheet" href="https://fonts.googleapis.com/css2?family=Raleway:wght@400;600&family=Open+Sans:wght@400;600&display=swap">
<style>
:root{
  --bg:#cfd0d2;
  --paper:#ffffff;
  --pink:#dc9a90;
  --pink-soft:#f3dcd6;
  --pink-band:#e8b3a9;
  --grey-text:#6f6f6f;
  --grey-name:#7d7d7d;
  --panel-grey:#f0efef;
  --rule:#e7c3bc;
}
*{box-sizing:border-box;margin:0;padding:0}
html,body{width:851px;height:1200px;overflow:hidden;background:var(--bg)}
body{position:relative;font-family:"Open Sans",Arial,sans-serif;color:var(--grey-text)}
.sheet{position:absolute;left:40px;width:770px;height:575px;background:var(--paper);display:flex;box-shadow:0 2px 6px rgba(0,0,0,.25)}
.sheet--outside{top:14px}
.sheet--inside{top:611px}
.panel{position:relative;width:256.67px;height:100%;overflow:hidden}
.panel + .panel{border-left:1px solid #eee}
.photo{position:absolute;left:0;right:0}
.heading{font-family:"Raleway",Arial,sans-serif;color:var(--pink);font-weight:600;font-size:8px;line-height:1.3;margin-bottom:4px}
.copy{font-size:5.6px;line-height:1.55;margin-bottom:8px}
.pad{position:absolute;left:14px;right:14px}
.expect-box{position:absolute;left:0;right:0;bottom:0;height:100px;background:var(--panel-grey);padding:14px}
.brand-name{text-align:center;font-family:"Raleway",Arial,sans-serif;font-weight:600;color:var(--grey-name);font-size:20px;line-height:1.25;letter-spacing:1px}
.clinic{text-align:center;font-size:5.5px;letter-spacing:1.2px;color:var(--grey-text);margin-top:8px}
.contact-line{font-size:5.8px;line-height:1.7;text-align:center}
.accent{color:var(--pink)}
.rule{height:1px;background:var(--rule);margin:10px 40px}
.social-dots{display:flex;justify-content:center;gap:5px;margin-top:3px}
.social-dots span{width:9px;height:9px;border-radius:50%;background:var(--pink)}
.tag-band{position:absolute;left:0;right:0;background:var(--pink-soft);padding:14px 18px;text-align:right}
.tag-band p{font-size:6.4px;line-height:1.55;color:var(--grey-text);margin-bottom:8px}
.site{position:absolute;right:18px;bottom:16px;font-size:6px;color:var(--pink)}
.bar{background:var(--pink-band);color:#fff;font-family:"Open Sans",Arial,sans-serif;font-weight:600;font-size:6.4px;letter-spacing:.3px;line-height:1.4;padding:4px 14px;margin:0 -14px 6px;white-space:nowrap}
.bar em{font-style:normal;font-weight:400}
.prices{list-style:none}
.prices li{display:flex;font-size:5.6px;line-height:1.75}
.prices li::after{content:"";order:1;flex:1;border-bottom:1px dotted #bbb;margin:0 3px 2px}
.prices li b{order:2;font-weight:600}
.block{position:absolute;left:14px;right:14px}
</style>
</head>
<body>

<section class="sheet sheet--outside">
  <div class="panel panel--about">
    <div class="pad" style="top:14px">
      <h2 class="heading">Wisp Laser Hair Removal with the Corvana GlideMark (TM)</h2>
      <p class="copy">The Corvana aesthetic division is a worldwide leader in energy-based aesthetic devices with presence in over 100 countries, as a pioneer in the field of aesthetic medicine. GlideMark (TM) is FDA approved and uses clinically proven diode laser technology to permanently remove unwanted hair comfortably, safely and effectively, for all skin colours and types – even with a tan.</p>
      <h2 class="heading">How it works:</h2>
      <p class="copy">The GlideMark (TM) is able to stop the growth of unwanted hair permanently, by delivering high-energy pulses to the hair follicle. This is achieved by targeting the melanin inside the follicle and heating it up until follicle damage occurs. Treatments are made comfortable by the patented Frost Nib Integrated Technology; a system that continuously cools the skin of the area being treated.</p>
    </div>
    <div class="photo" style="top:262px;height:190px;background:linear-gradient(135deg,#e9d6cc,#c9aa9b 60%,#efe3dc)" role="img" aria-label="Photo of a woman with smooth skin touching her face"></div>
    <div class="expect-box">
      <h2 class="heading">What to expect:</h2>
      <p class="copy">Laser Hair Removal requires multiple sessions (typically between 6 – 8), spaced approximately 6 weeks between each session.</p>
    </div>
  </div>

  <div class="panel panel--back">
    <div class="brand-name" style="margin-top:50px">WISP<br>Laser Hair Removal</div>
    <p class="clinic">MAPLEGROVE AESTHETIC CLINIC</p>
    <div class="rule" style="margin-top:22px"></div>
    <p class="contact-line">4860 Tollway Crescent,<br>Suite 115 London, ON</p>
    <div class="rule"></div>
    <p class="contact-line">For more information, visit us at<br><span class="accent">www.wisplaser-example.ca</span></p>
    <div class="rule"></div>
    <p class="contact-line">To book an appointment or free consultation:<br><span class="accent">Marisol@wisplaser-example.ca</span> &nbsp;|&nbsp; 555-013-8826</p>
    <div class="rule"></div>
    <p class="contact-line">Find us on</p>
    <div class="social-dots"><span></span><span></span></div>
    <p class="contact-line" style="margin-top:3px">WISP Laser Demo &nbsp;·&nbsp; IG: @wisplaserdemo</p>
    <div class="photo" style="top:330px;left:78px;right:78px;height:60px;background:radial-gradient(circle,#cfe0c0,#f6f9f2 70%)" role="img" aria-label="Small decorative leaf illustration"></div>
  </div>

  <div class="panel panel--cover">
    <div class="photo" style="top:0;height:340px;background:linear-gradient(160deg,#f1e6e1,#d9b9ab 55%,#b99283)" role="img" aria-label="Photo of a woman's smooth shoulders and back"></div>
    <div class="tag-band" style="top:340px;bottom:0">
      <p>Laser Hair Removal is an affordable, safe and effective way to treat unwanted hair – permanently!</p>
      <p>WISP uses the Corvana GlideMark(TM) Diode Laser – the Gold Standard in Laser Hair Removal!</p>
    </div>
    <div class="site">www.wisplaser-example.ca</div>
  </div>
</section>

<section class="sheet sheet--inside">
  <div class="panel panel--face-upper">
    <div class="block" style="top:14px">
      <div class="bar">FACE</div>
      <ul class="prices">
        <li>Upper Lip<b>$35</b></li>
        <li>Chin<b>$35</b></li>
        <li>Cheeks<b>$35</b></li>
        <li>Full Face (Lip/Chin/Cheeks)<b>$100</b></li>
        <li>Middle Brow<b>$25</b></li>
      </ul>
    </div>
    <div class="block" style="top:120px">
      <div class="bar">UPPER BODY <em>(above waist)</em></div>
      <ul class="prices">
        <li>Underarm<b>$75</b></li>
        <li>Chest<b>$150</b></li>
        <li>Full Arm<b>$150</b></li>
        <li>1/2 Arm<b>$100</b></li>
        <li>Areola<b>$50</b></li>
        <li>Full Back<b>$250</b></li>
        <li>Shoulders<b>$75</b></li>
        <li>Full Hands w/ Fingers<b>$50</b></li>
        <li>Fingers only<b>$25</b></li>
      </ul>
    </div>
    <div class="photo" style="top:250px;bottom:0;background:linear-gradient(150deg,#e3ccc4,#b99a90 50%,#d8c4bd)" role="img" aria-label="Photo of a laser treatment being applied to a client"></div>
  </div>

  <div class="panel panel--lower-women">
    <div class="block" style="top:14px">
      <div class="bar">LOWER BODY <em>(below the waist)</em></div>
      <ul class="prices">
        <li>Full Leg<b>$300</b></li>
        <li>Upper Leg<b>$175</b></li>
        <li>Lower Leg<b>$150</b></li>
        <li>Stomach<b>$150</b></li>
        <li>Navel and Navel Line<b>$50</b></li>
        <li>Navel and Lower Abdomen<b>$100</b></li>
        <li>Lower Back<b>$100</b></li>
        <li>Classic Bikini<b>$75</b></li>
        <li>Deep Bikini or Brazilian<b>$125</b></li>
        <li>Buttocks<b>$100</b></li>
        <li>Between cheeks<b>$75</b></li>
        <li>Full Feet w/ Toes<b>$50</b></li>
        <li>Toes Only<b>$25</b></li>
      </ul>
    </div>
    <div class="photo" style="top:205px;height:245px;background:linear-gradient(170deg,#efe4df,#d2b3a6 60%,#c4a193)" role="img" aria-label="Photo of a woman's smooth legs"></div>
    <div class="block" style="top:462px">
      <div class="bar">WOMEN <em>(common combinations)</em></div>
      <ul class="prices">
        <li>Full Arm w/ Underarm<b>$200</b></li>
        <li>Full Leg w/ Classic Bikini<b>$350</b></li>
        <li>Full Leg w/ Deep Bikini or Brazilian<b>$375</b></li>
        <li>Classic Bikini w/ Inner Thigh<b>$100</b></li>
        <li>Deep Bikini or Brazilian w/ Inner Thigh<b>$150</b></li>
      </ul>
    </div>
  </div>

  <div class="panel panel--men">
    <div class="brand-name" style="margin-top:26px;font-size:17px">WISP<br>Laser Hair Removal</div>
    <div class="photo" style="top:98px;height:300px;background:linear-gradient(150deg,#e6d3c9,#b38a73 55%,#d9c2b5)" role="img" aria-label="Photo of a man's smooth back and shoulders"></div>
    <div class="block" style="top:410px">
      <div class="bar">MEN <em>(common areas and combinations)</em></div>
      <ul class="prices">
        <li>1/2 Face &amp; Neck (front)<b>$100</b></li>
        <li>Cheeks &amp; Neck (front)<b>$75</b></li>
        <li>Full Neck<b>$75</b></li>
        <li>Nape of Neck<b>$50</b></li>
        <li>Shoulders<b>$75</b></li>
        <li>Full Back<b>$250</b></li>
        <li>Full Back &amp; Full Neck<b>$300</b></li>
        <li>Neck (nape) and Shoulders<b>$100</b></li>
        <li>Full Back, Neck and Buttocks<b>$375</b></li>
      </ul>
    </div>
  </div>
</section>

</body>
</html>
```